DESSERT FLYER

We need a flyer design for desserts and drinks for our restaurant.

We use Retro/rustic as main theme

Flyer must include all images, which are attached to this project. We also named correctly for each images, so you can use for each dish's title (docx file)
Must include our logo as well.

Flyer tittle is "DESSERT YUMM"

Please see our website for reference at mapleorchid.com.au

Flyer's printing size is A5 Vertical. Single Side

Restaurant

```html
<!DOCTYPE html>
<html lang="en">
<head>
<meta charset="utf-8">
<title>Maple Orchid – Dessert Yumm Flyer</title>
<link href="https://fonts.googleapis.com/css2?family=Rubik+Dirt&family=Josefin+Sans:wght@700&family=Alegreya+Sans+SC:wght@800&display=swap" rel="stylesheet">
<style>
  :root {
    --page-bg: #e9e9e9;
    --navy: #2d3441;
    --navy-dark: #232936;
    --teal: #2fb1b6;
    --orange: #e0874e;
    --wood-light: #ecebe8;
    --wood-line: #d4d2cd;
    --wood-brown: #6a3820;
    --wood-brown-dark: #4e2614;
    --card-border: #f7f5f2;
    --caption: #ffffff;
  }
  * { box-sizing: border-box; margin: 0; padding: 0; }
  html, body { width: 1200px; height: 1000px; overflow: hidden; background: var(--page-bg); }
  .flyer {
    position: absolute; left: 280px; top: 47px; width: 640px; height: 905px;
    background:
      repeating-linear-gradient(180deg, transparent 0 86px, var(--wood-line) 86px 88px),
      linear-gradient(90deg, #f2f1ee, var(--wood-light) 50%, #f3f2ef);
    box-shadow: 0 6px 18px rgba(0,0,0,.25);
    overflow: hidden;
  }
  .header {
    position: absolute; left: 0; top: 0; width: 640px; height: 220px;
    background: linear-gradient(160deg, var(--navy), var(--navy-dark));
  }
  .torn-edge { position: absolute; left: 0; top: 196px; width: 640px; height: 50px; }
  .brand {
    position: absolute; left: 40px; top: 78px; width: 250px; text-align: center;
    font-family: "Josefin Sans", sans-serif; font-weight: 700; color: var(--teal);
    font-size: 40px; line-height: 44px;
  }
  .brand-mark {
    display: inline-block; width: 10px; height: 10px; border-radius: 50%;
    background: var(--teal); margin-right: 8px; vertical-align: middle;
  }
  .title-rule { position: absolute; left: 340px; width: 270px; border-top: 1px dashed var(--orange); }
  .title-rule.top { top: 28px; }
  .title-rule.bottom { top: 172px; }
  .title {
    position: absolute; left: 340px; top: 40px; width: 270px; text-align: center;
    font-family: "Rubik Dirt", sans-serif; font-weight: 400; color: var(--teal);
    font-size: 54px; line-height: 58px;
  }
  .menu-card {
    position: absolute; width: 270px; height: 195px;
    border: 4px solid var(--card-border);
    background: linear-gradient(180deg, var(--wood-brown), var(--wood-brown-dark));
    box-shadow: 0 2px 5px rgba(0,0,0,.3);
  }
  .dish-photo { position: absolute; left: 8px; top: 8px; width: 246px; height: 118px; }
  .dish-name {
    position: absolute; left: 12px; bottom: 10px; width: 175px;
    font-family: "Alegreya Sans SC", sans-serif; font-weight: 800;
    color: var(--caption); font-size: 15px; line-height: 15px;
  }
  .dish-name small { font-size: 12px; }
  .dish-price {
    position: absolute; right: 12px; bottom: 12px;
    font-family: "Josefin Sans", sans-serif; font-weight: 700;
    color: var(--teal); font-size: 24px;
  }
  .col-1 { left: 40px; } .col-2 { left: 330px; }
  .row-1 { top: 252px; } .row-2 { top: 462px; } .row-3 { top: 672px; }
</style>
</head>
<body>
<main class="flyer">
  <header class="header">
    <div class="brand"><span class="brand-mark"></span>Maple<br>Orchid</div>
    <div class="title-rule top"></div>
    <h1 class="title">DESSERT<br>YUMM</h1>
    <div class="title-rule bottom"></div>
  </header>
  <svg class="torn-edge" viewBox="0 0 640 50" preserveAspectRatio="none" aria-hidden="true">
    <path d="M0 10 L30 4 L55 14 L90 6 L120 16 L160 8 L190 18 L230 9 L265 20 L300 10 L340 22 L375 12 L410 24 L450 14 L480 26 L520 16 L555 28 L590 18 L620 30 L640 22 L640 40 L600 36 L560 42 L520 34 L470 40 L420 32 L370 38 L320 30 L270 36 L220 28 L170 34 L120 26 L70 32 L30 24 L0 30 Z" fill="#dcdcdc"/>
    <path d="M0 0 L640 0 L640 18 L610 24 L575 14 L540 22 L500 12 L460 20 L420 10 L385 18 L345 8 L300 16 L260 6 L220 14 L180 4 L140 12 L100 2 L60 10 L25 2 L0 6 Z" fill="var(--navy-dark)"/>
  </svg>

  <article class="menu-card col-1 row-1">
    <div class="dish-photo" role="img" aria-label="Photo of banana fritters on a banana leaf" style="background:linear-gradient(135deg,#d69a4a,#e8b35c 50%,#4d7a2e)"></div>
    <h2 class="dish-name">Banana Fritter<br><small>with</small><br>Vanilla Ice-Cream</h2>
    <span class="dish-price">$6.90</span>
  </article>
  <article class="menu-card col-2 row-1">
    <div class="dish-photo" role="img" aria-label="Photo of banana sago pudding on a green leaf" style="background:linear-gradient(135deg,#3f8a2c,#f1f1ec 50%,#4f9236)"></div>
    <h2 class="dish-name">Banana Sago<br>Pudding <small>with</small><br>Peanut Topping</h2>
    <span class="dish-price">$6.90</span>
  </article>
  <article class="menu-card col-1 row-2">
    <div class="dish-photo" role="img" aria-label="Photo of black sticky rice with mango pieces" style="background:linear-gradient(120deg,#4a2a48,#6b4a6a 45%,#f2d04a)"></div>
    <h2 class="dish-name">Black Sticky Rice<br><small>with</small> Mango</h2>
    <span class="dish-price">$6.90</span>
  </article>
  <article class="menu-card col-2 row-2">
    <div class="dish-photo" role="img" aria-label="Photo of fried ice-cream in a glass bowl" style="background:linear-gradient(135deg,#1f2d2a,#3a4a3e 40%,#e9d6b8)"></div>
    <h2 class="dish-name">Fried Ice-Cream <small>with</small><br><small>Caramel/Chocolate/<br>Strawberry Topping</small></h2>
    <span class="dish-price">$6.90</span>
  </article>
  <article class="menu-card col-1 row-3">
    <div class="dish-photo" role="img" aria-label="Photo of Vietnamese drip coffee with coffee beans" style="background:linear-gradient(135deg,#d8cdbd,#9c8068 50%,#5a3f2c)"></div>
    <h2 class="dish-name">Vietnamese Coffee</h2>
    <span class="dish-price">$6.90</span>
  </article>
  <article class="menu-card col-2 row-3">
    <div class="dish-photo" role="img" aria-label="Photo of fresh young coconut juice on a table" style="background:linear-gradient(135deg,#8a3a22,#b56a4a 45%,#efe8d6)"></div>
    <h2 class="dish-name">Fresh Young<br>Coconut Juice</h2>
    <span class="dish-price">$5.50</span>
  </article>
</main>
</body>
</html>
```